Asphalt Driveway Billboard Design

We need a billboard designed for an Asphalt & Concrete Company in Minnesota. We want to advertise Asphalt Driveways on this billboard! Logo is uploaded below. Our website is tamlin-paving.com for more information.

```html
<!DOCTYPE html>
<html lang="en">
<head>
<meta charset="utf-8">
<title>Tamlin Asphalt &amp; Concrete – Billboard</title>
<link href="https://fonts.googleapis.com/css2?family=Archivo+Black&family=Montserrat:wght@700;800&family=Oswald:wght@600&family=Signika:wght@600&display=swap" rel="stylesheet">
<style>
  :root {
    --page-bg: #e9edf2;
    --board-white: #ffffff;
    --ink: #1f1f20;
    --brand-blue: #1a5aa6;
    --accent-cyan: #2a9fd8;
    --asphalt: #3b3c3f;
    --sky: #4f9be0;
    --siding: #c9b99a;
    --stone: #a08a72;
    --lawn: #5d8f3a;
  }
  * { margin: 0; padding: 0; box-sizing: border-box; }
  html, body { width: 1200px; height: 800px; overflow: hidden; }
  body { background: var(--page-bg); position: relative; }

  .billboard {
    position: absolute;
    left: 10px; top: 105px;
    width: 1180px; height: 590px;
    background: var(--board-white);
    box-shadow: 0 2px 10px rgba(0,0,0,.12);
  }
  .billboard__art { position: absolute; inset: 0; width: 100%; height: 100%; }

  .brand {
    position: absolute;
    left: 40px; width: 510px;
    text-align: center;
  }
  .brand__name {
    top: 150px;
    font-family: "Montserrat", sans-serif;
    font-weight: 800;
    color: var(--ink);
    line-height: 1;
  }
  .brand__name-main { display: block; font-size: 78px; letter-spacing: 2px; }
  .brand__name-sub { display: block; font-size: 22px; letter-spacing: 3px; margin-top: 14px; }

  .tagline {
    top: 375px;
    font-family: "Oswald", sans-serif;
    font-weight: 600;
    font-size: 38px;
    line-height: 48px;
    color: var(--ink);
    text-transform: uppercase;
  }
  .website {
    top: 490px;
    font-family: "Montserrat", sans-serif;
    font-weight: 700;
    font-size: 25px;
    color: var(--brand-blue);
  }

  .offer {
    position: absolute;
    left: 612px; width: 500px;
    text-align: center;
  }
  .offer__headline {
    top: 400px;
    font-family: "Signika", sans-serif;
    font-weight: 600;
    font-size: 42px;
    color: var(--accent-cyan);
  }
  .offer__phone {
    top: 468px;
    font-family: "Archivo Black", sans-serif;
    font-size: 46px;
    color: #ffffff;
    letter-spacing: 1px;
  }
</style>
</head>
<body>
  <section class="billboard">
    <svg class="billboard__art" viewBox="0 0 1180 590" preserveAspectRatio="none">
      <defs>
        <linearGradient id="driveway-scene" x1="0" y1="0" x2="0" y2="1">
          <stop offset="0" stop-color="var(--sky)"/>
          <stop offset="0.18" stop-color="#9cc8ec"/>
          <stop offset="0.3" stop-color="var(--siding)"/>
          <stop offset="0.55" stop-color="var(--stone)"/>
          <stop offset="0.66" stop-color="#555b4e"/>
          <stop offset="0.74" stop-color="var(--asphalt)"/>
          <stop offset="1" stop-color="var(--asphalt)"/>
        </linearGradient>
      </defs>
      <path class="swoosh" fill="var(--ink)"
            d="M782 31 Q570 220 560 370 Q558 490 610 555 L622 555 Q580 470 592 360 Q620 175 855 31 Z"/>
      <path class="driveway-photo" fill="url(#driveway-scene)" role="img"
            aria-label="Photo of a two-storey stone and siding house with a freshly paved black asphalt driveway and green lawn"
            d="M855 31 L1158 31 L1158 555 L622 555 Q580 470 592 360 Q620 175 855 31 Z"/>
    </svg>

    <h1 class="brand brand__name">
      <span class="brand__name-main">TAMLIN</span>
      <span class="brand__name-sub">ASPHALT &amp; CONCRETE</span>
    </h1>
    <p class="brand tagline">You deserve to come<br>home to quality</p>
    <p class="brand website">www.tamlin-paving.com</p>

    <p class="offer offer__headline">Free Quick Estimate</p>
    <p class="offer offer__phone">763-555-0148</p>
  </section>
</body>
</html>
```